Now Open Poster

We need a banner for our sports supplement and nutritional store, Harbor Nutrition.
We were hoping for some sort of creative word art piece.
I have drawn my own mock up just to give you all a very basic starting point. But you are free to go with whatever you feel will work best.
The primary objective is simply to explain a little about what the company does, and then direct traffic towards the store with an 'Open Arrow' pointing left.
Text words we have chosen are:
Protein
Creatine
Health
Fitness
Sports Science
Nutrition
Energy
Achievement
Amino Acids
Organic
Supplements
Performance
Testosterone Support
Vitamins
Growth
Diet
Happiness
Weight Loss
Strong
Natural
Vitality
Accomplished
Below the word art we want our logo (See attached options)
Then below the logo the phrase "Success Starts Here"
Dimensions of the poster are 140cm x 60cm.
Colours: Blues/Whites/Greys/Blacks (Lots of white space please)
Here are some cool pieces I found that had some interesting elements that I liked (I'd love to see a mash-up of styles with a street art feel to it. Something funky!):
http://www.moodgrove.example/pin/804417263190552871/
http://www.moodgrove.example/pin/615380924471208539/
http://www.moodgrove.example/pin/804417263192736155/
http://www.moodgrove.example/pin/804417263194418620/
http://www.moodgrove.example/pin/937162048856301742/
Thanks for reading, message me if you have any further questions!
- Tobias

```html
<!DOCTYPE html>
<html lang="en">
<head>
<meta charset="utf-8">
<title>Harbor Nutrition – Now Open Banners</title>
<link rel="stylesheet" href="https://fonts.googleapis.com/css2?family=Bebas+Neue&family=Anton&display=swap">
<style>
  :root {
    --stage-blue: #0a7cc0;
    --brand-blue: #1a86d0;
    --ink: #111111;
    --paper: #f4f3f0;
    --slash-grey: #9a9a9a;
    --frame: #222222;
  }
  * { margin: 0; padding: 0; box-sizing: border-box; }
  html, body { width: 1200px; height: 1000px; overflow: hidden; }
  body { background: var(--stage-blue); position: relative; font-family: "Bebas Neue", "Arial Narrow", sans-serif; }

  .banner {
    position: absolute; top: 10px; width: 420px; height: 980px;
    background: var(--paper); border: 1.5px solid var(--frame);
  }
  .banner--left { left: 150px; }
  .banner--right { left: 630px; }

  .banner__header {
    position: absolute; top: 0; left: 0; right: 0; height: 62px;
    border-bottom: 1.5px solid var(--frame);
    display: flex; align-items: center; justify-content: center; gap: 26px;
  }
  .banner__footer {
    position: absolute; bottom: 0; left: 0; right: 0; height: 62px;
    border-top: 1.5px solid var(--frame);
    display: flex; align-items: center; justify-content: center; gap: 8px;
    font-size: 31px; letter-spacing: 0.5px;
  }
  .chevrons {
    color: var(--ink); font-family: "Anton", "Impact", sans-serif;
    font-size: 26px; letter-spacing: -3px; display: inline-block; transform: scaleX(0.75) skewX(-10deg);
  }
  .open-label { color: var(--brand-blue); font-size: 38px; letter-spacing: 1px; }
  .footer-slashes {
    color: var(--ink); font-family: "Anton", "Impact", sans-serif;
    font-size: 26px; letter-spacing: -1px; display: inline-block; transform: skewX(-12deg);
  }
  .footer-phrase { color: var(--brand-blue); }

  .word-art {
    position: absolute; top: 68px; left: 0; right: 0;
    list-style: none; text-align: center;
  }
  .word-art li { font-size: 34px; line-height: 32.65px; height: 32.65px; letter-spacing: 0.3px; }
  .word-art li:nth-child(odd) { color: var(--ink); }
  .word-art li:nth-child(even) { color: var(--brand-blue); }

  .slogan {
    position: absolute; font-family: "Anton", "Impact", sans-serif; color: var(--ink);
    font-size: 54px; letter-spacing: 4px; white-space: nowrap;
    transform: translate(-50%, -50%) rotate(-90deg);
  }
  .slogan--strong { left: 45px; top: 460px; }
  .slogan--harbor { left: 375px; top: 462px; }

  .slash-group { position: absolute; width: 62px; height: 126px; }

  .brand-mark {
    position: absolute; left: 161px; top: 800px; width: 98px; height: 98px;
    border: 1.5px solid var(--ink); border-radius: 50%;
    display: flex; align-items: center; justify-content: center; text-align: center;
    font-family: "Bebas Neue", sans-serif; color: var(--ink); font-size: 19px; line-height: 19px;
  }
</style>
</head>
<body>

  <section class="banner banner--left">
    <header class="banner__header">
      <span class="chevrons">&lt;&lt;&lt;&lt;&lt;&lt;&lt;&lt;&lt;&lt;</span>
      <span class="open-label">OPEN</span>
      <span class="chevrons">&lt;&lt;&lt;&lt;&lt;&lt;&lt;&lt;&lt;&lt;</span>
    </header>

    <svg class="slash-group" style="left:14px;top:105px" viewBox="0 0 62 126" aria-hidden="true">
      <g stroke="#9a9a9a" stroke-width="9"><line x1="2" y1="26" x2="60" y2="6"/><line x1="2" y1="51" x2="60" y2="31"/><line x1="2" y1="76" x2="60" y2="56"/><line x1="2" y1="101" x2="60" y2="81"/><line x1="2" y1="124" x2="60" y2="104"/></g>
    </svg>
    <svg class="slash-group" style="left:14px;top:670px" viewBox="0 0 62 126" aria-hidden="true">
      <g stroke="#9a9a9a" stroke-width="9"><line x1="2" y1="26" x2="60" y2="6"/><line x1="2" y1="51" x2="60" y2="31"/><line x1="2" y1="76" x2="60" y2="56"/><line x1="2" y1="101" x2="60" y2="81"/><line x1="2" y1="124" x2="60" y2="104"/></g>
    </svg>
    <svg class="slash-group" style="left:344px;top:140px" viewBox="0 0 62 126" aria-hidden="true">
      <g stroke="#9a9a9a" stroke-width="9"><line x1="2" y1="26" x2="60" y2="6"/><line x1="2" y1="51" x2="60" y2="31"/><line x1="2" y1="76" x2="60" y2="56"/><line x1="2" y1="101" x2="60" y2="81"/><line x1="2" y1="124" x2="60" y2="104"/></g>
    </svg>
    <svg class="slash-group" style="left:344px;top:635px" viewBox="0 0 62 126" aria-hidden="true">
      <g stroke="#9a9a9a" stroke-width="9"><line x1="2" y1="26" x2="60" y2="6"/><line x1="2" y1="51" x2="60" y2="31"/><line x1="2" y1="76" x2="60" y2="56"/><line x1="2" y1="101" x2="60" y2="81"/><line x1="2" y1="124" x2="60" y2="104"/></g>
    </svg>

    <div class="slogan slogan--strong">I AM STRONG</div>
    <div class="slogan slogan--harbor">I AM HARBOR</div>

    <ul class="word-art">
      <li>Protein</li><li>Creatine</li><li>Health</li><li>Fitness</li><li>Sports Science</li><li>Nutrition</li><li>Energy</li><li>Achievement</li><li>Amino Acids</li><li>Organic</li><li>Supplements</li><li>Performance</li><li>Testosterone Support</li><li>Vitamins</li><li>Growth</li><li>Diet</li><li>Happiness</li><li>Weight Loss</li><li>Strong</li><li>Natural</li><li>Vitality</li><li>Accomplished</li>
    </ul>

    <div class="brand-mark">Harbor<br>Nutrition</div>

    <footer class="banner__footer">
      <span class="footer-slashes">/////</span>
      <span class="footer-phrase">SUCCESS STARTS HERE</span>
      <span class="footer-slashes">/////</span>
    </footer>
  </section>

  <section class="banner banner--right">
    <header class="banner__header">
      <span class="chevrons">&lt;&lt;&lt;&lt;&lt;&lt;&lt;&lt;&lt;&lt;</span>
      <span class="open-label">OPEN</span>
      <span class="chevrons">&lt;&lt;&lt;&lt;&lt;&lt;&lt;&lt;&lt;&lt;</span>
    </header>

    <ul class="word-art">
      <li>Protein</li><li>Creatine</li><li>Health</li><li>Fitness</li><li>Sports Science</li><li>Nutrition</li><li>Energy</li><li>Achievement</li><li>Amino Acids</li><li>Organic</li><li>Supplements</li><li>Performance</li><li>Testosterone Support</li><li>Vitamins</li><li>Growth</li><li>Diet</li><li>Happiness</li><li>Weight Loss</li><li>Strong</li><li>Natural</li><li>Vitality</li><li>Accomplished</li>
    </ul>

    <div class="brand-mark">Harbor<br>Nutrition</div>

    <footer class="banner__footer">
      <span class="footer-slashes">/////</span>
      <span class="footer-phrase">SUCCESS STARTS HERE</span>
      <span class="footer-slashes">/////</span>
    </footer>
  </section>

</body>
</html>
```